Fernlake Business Card Design

We are looking for a fresh business card design for our new logo. We would like a business card that is unique but friendly. We are in the window coverings business offering blinds, shutters and shades for homes.

Target Market(s)

Targeting the end-consumer

Industry/Entity Type

Business

Requirements
Must have
• Must have a dedicates space for a photo of our sales person. Must contain our new logo (attached).

```html
<!DOCTYPE html>
<html lang="en">
<head>
<meta charset="utf-8">
<title>Fernlake Business Card</title>
<link href="https://fonts.googleapis.com/css2?family=Lato:wght@400&family=Roboto:wght@400&family=Roboto+Condensed:wght@500;700&display=swap" rel="stylesheet">
<style>
  :root {
    --backdrop: #2b2b2b;
    --card-white: #f2f2f2;
    --leaf-green: #86bf3c;
    --slate: #7a7a7a;
    --ink: #555555;
    --photo-light: #b4b4b4;
    --photo-dark: #8a8a8a;
    --white: #ffffff;
  }
  html, body {
    margin: 0;
    width: 1200px;
    height: 960px;
    overflow: hidden;
    background: var(--backdrop);
  }
  .card {
    position: absolute;
    width: 600px;
    height: 342px;
    overflow: hidden;
    box-shadow: 0 3px 8px rgba(0,0,0,0.5);
  }
  .card--front { left: 314px; top: 113px; background: var(--card-white); }
  .card--back  { left: 311px; top: 472px; background: var(--leaf-green); }

  .brand {
    position: absolute;
    left: 41px;
    top: 47px;
    display: flex;
    align-items: center;
    gap: 12px;
  }
  .brand__mark {
    width: 46px;
    height: 46px;
    background: var(--leaf-green);
    border-radius: 4px;
  }
  .brand__name {
    font-family: "Lato", sans-serif;
    font-size: 40px;
    color: var(--slate);
    line-height: 1;
  }

  .address {
    position: absolute;
    left: 40px;
    top: 151px;
    font-family: "Roboto", sans-serif;
    font-size: 14px;
    line-height: 18px;
    color: var(--ink);
    margin: 0;
  }
  .contacts {
    position: absolute;
    left: 40px;
    top: 197px;
    margin: 0;
    padding: 0;
    list-style: none;
    font-family: "Roboto", sans-serif;
    font-size: 14px;
    line-height: 19px;
    color: var(--ink);
  }
  .contacts li { display: flex; align-items: center; gap: 9px; }
  .contacts svg { width: 14px; height: 14px; fill: var(--leaf-green); flex: none; }

  .salesperson-photo {
    position: absolute;
    left: 350px;
    top: 20px;
    width: 250px;
    height: 272px;
    background: linear-gradient(180deg, var(--photo-light), var(--photo-dark));
    border-radius: 60px 60px 0 0;
  }

  .footer-band { position: absolute; left: 0; bottom: 0; width: 600px; height: 52px; }

  .person {
    position: absolute;
    left: 340px;
    width: 260px;
    top: 296px;
    text-align: center;
    color: var(--white);
    font-family: "Roboto Condensed", sans-serif;
  }
  .person__name { font-size: 21px; font-weight: 500; line-height: 22px; }
  .person__title { font-size: 15px; font-weight: 500; line-height: 20px; }

  .back-brand {
    position: absolute;
    left: 0;
    width: 600px;
    top: 150px;
    text-align: center;
    font-family: "Lato", sans-serif;
    font-size: 46px;
    color: var(--white);
  }
  .back-web {
    position: absolute;
    left: 0;
    width: 600px;
    top: 288px;
    text-align: center;
    font-family: "Roboto", sans-serif;
    font-size: 14px;
    letter-spacing: 5px;
    color: var(--white);
  }
</style>
</head>
<body>
  <section class="card card--front">
    <div class="brand">
      <span class="brand__mark"></span>
      <span class="brand__name">Fernlake</span>
    </div>

    <p class="address">2140 Cedar Hollow Road<br>Juneau, Alaska 99801</p>

    <ul class="contacts">
      <li><svg viewBox="0 0 14 14"><path d="M3 1l2.5 3-1.5 1.5c.8 1.8 2.2 3.2 4 4L9.5 8l3 2.5-1.5 2.5C6 13 1 8 .5 2.5z"/></svg>907 555 0142</li>
      <li><svg viewBox="0 0 14 14"><path d="M4 0h6a1 1 0 011 1v12a1 1 0 01-1 1H4a1 1 0 01-1-1V1a1 1 0 011-1zm.5 1.5v9.5h5V1.5z"/></svg>907 555 0178</li>
      <li><svg viewBox="0 0 14 14"><path d="M3 0h8v4H3zM0 5h14v6h-3v3H3v-3H0zm4 4v4h6V9z"/></svg>907 555 0193</li>
      <li><svg viewBox="0 0 14 14"><path d="M0 3h14v8H0zm1.5 1.2L7 8l5.5-3.8V4h-11z"/></svg>name@fernlake.com</li>
      <li><svg viewBox="0 0 14 14"><circle cx="7" cy="7" r="6.5"/></svg>www.fernlake.com</li>
    </ul>

    <div class="salesperson-photo" role="img" aria-label="Photo of the sales person"></div>

    <svg class="footer-band" viewBox="0 0 600 52" aria-hidden="true">
      <rect x="0" y="23" width="320" height="13" fill="var(--slate)"/>
      <path d="M0 38 H300 C315 38 318 0 345 0 H600 V52 H0 Z" fill="var(--leaf-green)"/>
      <path d="M0 36 H300 C315 36 318 -2 345 -2" stroke="var(--white)" stroke-width="2" fill="none"/>
    </svg>

    <div class="person">
      <div class="person__name">DANA WHITLOW</div>
      <div class="person__title">CEO/FOUNDER</div>
    </div>
  </section>

  <section class="card card--back">
    <div class="back-brand">Fernlake</div>
    <div class="back-web">www.fernlake.com</div>
  </section>
</body>
</html>
```